Elegant brochure design for startup

We want to design an advertising booklet to introduce our company as a professional and trustworthy.

please take a look at the attached content templet to read know more about our business and services. Also to see what each page of the booklet should contain.

The size of the booklet should be around the half of A4 page. 12 pages includes the cover and back page ( See content templet attached )

We will provide content, pictures, and logo and our specifications for the
designer

Target Market(s)

We want to target executives in private and government sectors, the decision makers who are open to new and fresh ideas

Industry/Entity Type

Business Consultant

Font styles to use
Sans Serif

Requirements
Must have
• - Attractive, elegant, eyes catching design inspired attached identity.
• - bright color background for the writhing to make it easier for readers
• - neat arrangement of the content throughout the booklet. For example, arranging the content in a boxes using colors etc. to make easier for the reader.
Nice to have
• - icons to explane some of the content.
• - Info-graphic style when it make the content (in some parts easer to read )
• - Simple and elegant
• - We have a simi human icon as the letter "i" in our logo .. you may use it in some forms to represent human icon. Also you can modify it to represent deferent human format (Doctors - women - factory employee etc.
Should not have
• - don't use human pictures ! we prefer to use graphic abstract shapes and colors.
• - We don't prefer crowded pages ..
• - Our work is all about LOCAL organizational culture and employees. We are taking about the local market and as you know our local uniform is deferent than the western dress uniform. That's way we don't want to put a pic with a man in suit or women in short uniform. You can use icon like the ones when you search ( saudi employee icon) (without showing the faces - shadow format)

```html
<!DOCTYPE html>
<html lang="en">
<head>
<meta charset="utf-8">
<title>Clearpath Workplace Brochure</title>
<link href="https://fonts.googleapis.com/css2?family=Raleway:ital,wght@0,400;0,600;0,700;0,800;1,400;1,700;1,800&display=swap" rel="stylesheet">
<style>
:root{
  --sky:#1ea3e0;
  --sky-soft:#5cc0ec;
  --navy:#0e3b6a;
  --mid:#176fae;
  --ink:#3a3a3a;
  --paper:#ffffff;
  --backdrop:#ebe9e5;
  --photo-dark:#1d2a30;
  --photo-light:#8a9a8c;
}
*{box-sizing:border-box;margin:0;padding:0}
html,body{width:1200px;height:2358px;overflow:hidden;background:var(--backdrop);font-family:"Raleway",Arial,sans-serif;color:var(--ink)}
.spread{position:absolute;left:50px;width:1100px;height:530px;display:flex;box-shadow:0 10px 28px rgba(0,0,0,.28)}
.page{position:relative;width:550px;height:530px;background:var(--paper);overflow:hidden}
.page--left{box-shadow:inset -18px 0 22px -18px rgba(0,0,0,.25)}
.page--right{box-shadow:inset 18px 0 22px -18px rgba(0,0,0,.25)}

/* side strips */
.strip{position:absolute;top:0;width:70px;height:530px}
.strip--right{right:0}
.strip--left{left:0}
.strip__brand{position:absolute;top:0;left:0;width:70px;height:300px;background:var(--navy);display:flex;align-items:center;justify-content:center}
.strip__tag{position:absolute;top:300px;left:0;width:70px;height:230px;background:var(--sky);display:flex;align-items:center;justify-content:center}
.vertical{writing-mode:vertical-rl;transform:rotate(180deg);white-space:nowrap;color:#fff}
.vertical--brand{font-weight:700;font-size:19px;letter-spacing:.5px}
.vertical--tag{font-weight:400;font-size:19px;letter-spacing:.5px;opacity:.9}

/* photo */
.photo{position:absolute;top:0;left:0;width:480px;height:250px;background:linear-gradient(160deg,var(--photo-light) 0%,var(--photo-dark) 55%,#3d4a40 100%)}

/* generic text */
.copy{position:absolute;font-size:11.5px;line-height:1.45;color:var(--ink)}
.copy b{color:var(--navy);font-weight:800}
.heading-bar{position:absolute;height:26px;padding:0 18px;display:flex;align-items:center;color:#fff;font-weight:700;font-size:15px}
.heading-bar--sky{background:var(--sky)}
.heading-bar--navy{background:var(--navy)}

/* spread 1 */
.pillar{position:absolute;left:0;width:550px;height:120px;background:var(--sky)}
.pillar__word{position:absolute;left:40px;top:40px;font-size:32px;font-weight:800;font-style:italic;color:#fff;letter-spacing:.5px}
.pillar__note{position:absolute;left:240px;top:0;width:310px;height:120px;background:var(--navy);clip-path:polygon(22% 0,100% 0,100% 100%,0 100%);padding:18px 18px 0 100px;color:#fff;font-size:11.5px;line-height:1.35;text-transform:uppercase}

/* service lists */
.service-list{position:absolute;list-style:none}
.service-list li{display:flex;align-items:center;gap:10px;font-size:11.5px;font-weight:700;font-style:italic;color:#222;height:29px}
.glyph{width:20px;height:20px;flex:none}

/* why page */
.benefit{position:absolute;left:100px;width:420px;height:90px}
.benefit__label{position:absolute;left:0;top:26px;display:flex;gap:8px;font-size:11px;text-transform:uppercase;line-height:1.35;width:190px}
.benefit__icon{position:absolute;left:230px;top:0;width:90px;height:90px}

/* services steps */
.step{position:absolute;left:95px;width:430px;height:100px;border-bottom:1px dashed #9aa}
.step__num{position:absolute;left:0;top:6px;width:26px;height:26px;border-radius:50%;background:var(--navy);color:#fff;font-weight:800;font-size:14px;display:flex;align-items:center;justify-content:center}
.step__label{position:absolute;left:0;top:34px;width:130px;height:34px;background:var(--navy);color:#fff;font-size:10px;font-weight:700;text-transform:uppercase;padding:5px 10px;line-height:1.2}
.step__text{position:absolute;left:160px;top:8px;width:260px;font-size:11px;line-height:1.4;font-style:italic}

/* outsourcing */
.bpo{position:absolute;left:40px;width:400px;height:88px}
.bpo__tag{position:absolute;left:0;top:8px;width:140px;height:42px;color:#fff;font-size:10px;font-weight:700;text-transform:uppercase;padding:6px 10px;line-height:1.25;clip-path:polygon(0 0,90% 0,100% 50%,90% 100%,0 100%)}
.bpo__tag--navy{background:var(--navy)}
.bpo__tag--sky{background:var(--sky)}
.bpo__dot{position:absolute;left:162px;top:16px;width:24px;height:24px}
.bpo__text{position:absolute;left:200px;top:4px;width:200px;font-size:10.5px;line-height:1.4}
.timeline{position:absolute;left:213px;top:80px;width:2px;height:400px;background:#b7c2cc}
</style>
</head>
<body>

<!-- Spread 1 -->
<section class="spread" style="top:44px">
  <div class="page page--left">
    <div class="pillar" style="top:30px">
      <span class="pillar__word">ATTRACT</span>
      <p class="pillar__note">The top talent available in the workforce market by optimizing their workplace to become a workplace of choice.</p>
    </div>
    <div class="pillar" style="top:205px">
      <span class="pillar__word">ENGAGE</span>
      <p class="pillar__note">Human capital to the best of their abilities and increase performance and productivity.</p>
    </div>
    <div class="pillar" style="top:380px">
      <span class="pillar__word">RETAIN</span>
      <p class="pillar__note">The top talent by connecting them mentally and emotionally to their workplace.</p>
    </div>
  </div>
  <div class="page page--right">
    <div class="photo" role="img" aria-label="Photograph of a modern glass office building facade at dusk"></div>
    <div class="strip strip--right">
      <div class="strip__brand"><span class="vertical vertical--brand">CLEARPATH WORKPLACE</span></div>
      <div class="strip__tag"><span class="vertical vertical--tag">attract | empower | retain</span></div>
    </div>
    <p class="copy" style="left:40px;top:272px;width:410px"><b>CLEARPATH WORKPLACE</b> is a team of employee-engagement, internal communication, and organizational culture experts with both local and international backgrounds. With our expertise and longstanding experience, we can help organizations like yours to diagnose problems optimally, to measure your employee-engagement level, and to handle workplace-related challenges in organizational culture and internal communications.</p>
    <p class="copy" style="left:40px;top:400px;width:410px">We know the right practices and the path that leads to business success and high employee-engagement rates. We are willing to work side by side with you to help you achieve your goals, attract and engage the right candidates, align them with your organization's values and objectives, and create the best organizational culture to guarantee high retention rates.</p>
  </div>
</section>

<!-- Spread 2 -->
<section class="spread" style="top:624px">
  <div class="page page--left">
    <div class="strip strip--left">
      <div class="strip__brand"><span class="vertical vertical--brand">CLEARPATH WORKPLACE</span></div>
      <div class="strip__tag"><span class="vertical vertical--tag">attract | empower | retain</span></div>
    </div>
    <p class="copy" style="left:95px;top:22px;width:420px;font-size:10.5px;font-style:italic"><b>CLEARPATH WORKPLACE</b> provides professional business services focusing mainly on improving the workplace environment and increasing the level of employee engagement by using best practice from various related areas, such as:</p>
    <ul class="service-list" style="left:95px;top:80px">
      <li><svg class="glyph" viewBox="0 0 20 20"><rect width="20" height="20" fill="#1ea3e0"/><path d="M5 10l3 3 7-7" stroke="#fff" stroke-width="2" fill="none"/></svg>Employee-Engagement Surveys</li>
      <li><svg class="glyph" viewBox="0 0 20 20"><rect width="20" height="20" fill="#1ea3e0"/><path d="M4 6h12v7H9l-3 3v-3H4z" fill="#fff"/></svg>Internal Communications</li>
      <li><svg class="glyph" viewBox="0 0 20 20"><rect width="20" height="20" fill="#1ea3e0"/><rect x="4" y="4" width="5" height="5" fill="#fff"/><rect x="11" y="4" width="5" height="5" fill="#fff"/><rect x="4" y="11" width="5" height="5" fill="#fff"/><rect x="11" y="11" width="5" height="5" fill="#fff"/></svg>Organizational Culture</li>
      <li><svg class="glyph" viewBox="0 0 20 20"><rect width="20" height="20" fill="#1ea3e0"/><circle cx="10" cy="8" r="4" fill="#fff"/><path d="M7 11l-1 6 4-2 4 2-1-6z" fill="#fff"/></svg>Recognition and Reward</li>
    </ul>
    <p class="copy" style="left:95px;top:218px;width:420px;font-size:10.5px;font-style:italic">In addition, our services include business process outsourcing of various business functionalities to help companies focus on their core business. These services include:</p>
    <ul class="service-list" style="left:95px;top:262px">
      <li><svg class="glyph" viewBox="0 0 20 20"><rect width="20" height="20" fill="#176fae"/><path d="M4 10h9M10 6l4 4-4 4" stroke="#fff" stroke-width="2" fill="none"/></svg>Human Resources Outsourcing</li>
      <li><svg class="glyph" viewBox="0 0 20 20"><rect width="20" height="20" fill="#176fae"/><path d="M4 10h9M10 6l4 4-4 4" stroke="#fff" stroke-width="2" fill="none"/></svg>Specialized Training and Coaching</li>
      <li><svg class="glyph" viewBox="0 0 20 20"><rect width="20" height="20" fill="#176fae"/><path d="M4 10h9M10 6l4 4-4 4" stroke="#fff" stroke-width="2" fill="none"/></svg>Back- and Front-Office Outsourcing</li>
    </ul>
    <p class="copy" style="left:125px;top:360px;font-weight:700;font-style:italic;color:var(--mid)">Customer Experience Auditing</p>
  </div>
  <div class="page page--right">
    <div class="photo" role="img" aria-label="Photograph of a modern glass office building facade at dusk"></div>
    <div class="strip strip--right">
      <div class="strip__brand"><span class="vertical vertical--brand">CLEARPATH WORKPLACE</span></div>
      <div class="strip__tag"><span class="vertical vertical--tag">attract | empower | retain</span></div>
    </div>
    <div class="heading-bar heading-bar--sky" style="left:20px;top:262px">Our Mission</div>
    <p class="copy" style="left:40px;top:300px;width:410px">Our mission is to enable an organization's human capital to play the biggest possible role in its success.</p>
    <p class="copy" style="left:40px;top:340px;width:410px">We are dedicated to helping organizations become more successful through their human capital and by implementing the methods and strategies to make that human capital play the most significant role in the organization's success.</p>
    <div class="heading-bar heading-bar--navy" style="left:20px;top:410px">Our Social Responsibility</div>
    <p class="copy" style="left:40px;top:448px;width:410px">We aspire to contribute to the national strategy aimed at reducing the unemployment rate by helping organizations to add sustainable, high-quality jobs to the Saudi market.</p>
  </div>
</section>

<!-- Spread 3 -->
<section class="spread" style="top:1204px">
  <div class="page page--left">
    <div class="strip strip--left">
      <div class="strip__brand"><span class="vertical vertical--brand">CLEARPATH WORKPLACE</span></div>
      <div class="strip__tag"><span class="vertical vertical--tag">attract | empower | retain</span></div>
    </div>
    <div class="heading-bar heading-bar--sky" style="left:120px;top:20px">Why Clearpath Workplace?</div>
    <p class="copy" style="left:110px;top:56px;width:400px;font-style:italic;font-size:11px">Every workplace can become an <b>CLEARPATH WORKPLACE</b> if its business leaders have a clear understanding of their workplace's defects and a desire to implement the right practices to correct and improve their workforce. We can help you optimize your workplace to:</p>
    <div class="benefit" style="top:130px">
      <div class="benefit__label"><svg width="14" height="12" viewBox="0 0 14 12"><path d="M1 6l4 4 8-9" stroke="#0e3b6a" stroke-width="2" fill="none"/></svg>Drive innovation within your organization</div>
      <svg class="benefit__icon" viewBox="0 0 90 90"><circle cx="45" cy="45" r="42" fill="none" stroke="#0e3b6a" stroke-width="6" stroke-dasharray="180 300"/><circle cx="45" cy="45" r="35" fill="#1ea3e0"/><circle cx="45" cy="40" r="12" fill="#fff"/><rect x="39" y="52" width="12" height="8" fill="#fff"/></svg>
    </div>
    <div class="benefit" style="top:250px">
      <div class="benefit__label"><svg width="14" height="12" viewBox="0 0 14 12"><path d="M1 6l4 4 8-9" stroke="#0e3b6a" stroke-width="2" fill="none"/></svg>Increase employee productivity significantly</div>
      <svg class="benefit__icon" viewBox="0 0 90 90"><circle cx="45" cy="45" r="42" fill="none" stroke="#0e3b6a" stroke-width="6" stroke-dasharray="180 300"/><circle cx="45" cy="45" r="35" fill="#1ea3e0"/><rect x="28" y="50" width="7" height="12" fill="#fff"/><rect x="40" y="44" width="7" height="18" fill="#fff"/><rect x="52" y="38" width="7" height="24" fill="#fff"/><path d="M26 44l14-10 8 6 14-12" stroke="#fff" stroke-width="3" fill="none"/></svg>
    </div>
    <div class="benefit" style="top:370px">
      <div class="benefit__label"><svg width="14" height="12" viewBox="0 0 14 12"><path d="M1 6l4 4 8-9" stroke="#0e3b6a" stroke-width="2" fill="none"/></svg>Drive business results</div>
      <svg class="benefit__icon" viewBox="0 0 90 90"><circle cx="45" cy="45" r="42" fill="none" stroke="#0e3b6a" stroke-width="6" stroke-dasharray="180 300"/><circle cx="45" cy="45" r="35" fill="#1ea3e0"/><rect x="28" y="28" width="30" height="34" fill="#fff"/><rect x="33" y="35" width="20" height="3" fill="#1ea3e0"/><rect x="33" y="42" width="20" height="3" fill="#1ea3e0"/><circle cx="56" cy="56" r="7" fill="none" stroke="#0e3b6a" stroke-width="3"/></svg>
    </div>
  </div>
  <div class="page page--right">
    <div class="photo" role="img" aria-label="Photograph of a modern glass office building facade at dusk"></div>
    <div class="strip strip--right">
      <div class="strip__brand"><span class="vertical vertical--brand">CLEARPATH WORKPLACE</span></div>
      <div class="strip__tag"><span class="vertical vertical--tag">attract | empower | retain</span></div>
    </div>
    <div class="heading-bar heading-bar--navy" style="left:20px;top:262px">We Understand The Local Workforce</div>
    <p class="copy" style="left:40px;top:310px;width:410px">After communicating, interviewing, and working closely with thousands of local employees in relation to workplace challenges and opportunities, we have a keen understanding of the local workforce and market.</p>
    <p class="copy" style="left:70px;top:390px;width:360px;font-size:14px;text-align:center;line-height:1.4">We can point you toward the pathways that lead to the <b>CLEARPATH WORKPLACE</b> and organizational success</p>
  </div>
</section>

<!-- Spread 4 -->
<section class="spread" style="top:1784px">
  <div class="page page--left">
    <div class="strip strip--left">
      <div class="strip__brand"><span class="vertical vertical--brand">CLEARPATH WORKPLACE</span></div>
      <div class="strip__tag"><span class="vertical vertical--tag">attract | empower | retain</span></div>
    </div>
    <div class="heading-bar heading-bar--sky" style="left:95px;top:14px">Our Services</div>
    <div class="step" style="top:50px">
      <span class="step__num">1</span><span class="step__label">Assessment and Feedback</span>
      <p class="step__text">Assessment and feedback that studies the different components of the organization by collecting information, using surveys and other tools that help to determine the health status of your workplace environment.</p>
    </div>
    <div class="step" style="top:160px">
      <span class="step__num">2</span><span class="step__label">Analysis and Diagnostics</span>
      <p class="step__text">Analysis and diagnostics of insights using our comprehensive metrics to determine the areas that need to be improved and to determine the right solutions.</p>
    </div>
    <div class="step" style="top:270px">
      <span class="step__num">3</span><span class="step__label">Execution</span>
      <p class="step__text">Implementation of a Workplace Optimization Plan, using the right combination of solutions that fit your organization best, as advised by our experts.</p>
    </div>
    <div class="step" style="top:380px;border-bottom:none">
      <span class="step__num">4</span><span class="step__label">Measurement and Tuning</span>
      <p class="step__text">Measurement and fine tuning of results after applying our solutions, measured through specific KPIs that allow you to stay focused and gain insights into the continuous improvements that assure maximum talent engagement in achieving your organization's mission.</p>
    </div>
  </div>
  <div class="page page--right">
    <div class="strip strip--right">
      <div class="strip__brand"><span class="vertical vertical--brand">CLEARPATH WORKPLACE</span></div>
      <div class="strip__tag"><span class="vertical vertical--tag">attract | empower | retain</span></div>
    </div>
    <div class="heading-bar heading-bar--navy" style="left:30px;top:14px">Business Process Outsourcing</div>
    <p class="copy" style="left:40px;top:46px;width:410px;font-size:11px">We can help you to focus on developing the company's core business by outsourcing some of your business processes to us.</p>
    <div class="timeline"></div>
    <div class="bpo" style="top:84px">
      <span class="bpo__tag bpo__tag--navy">Human Resources</span>
      <svg class="bpo__dot" viewBox="0 0 24 24"><circle cx="12" cy="12" r="12" fill="#0e3b6a"/><path d="M7 12h9M13 8l4 4-4 4" stroke="#fff" stroke-width="2" fill="none"/></svg>
      <p class="bpo__text">Our experts will help you with interviewing, assessing, and selecting talent suited to your culture.</p>
    </div>
    <div class="bpo" style="top:186px">
      <span class="bpo__tag bpo__tag--sky">Specialized Training and Coaching</span>
      <svg class="bpo__dot" viewBox="0 0 24 24"><circle cx="12" cy="12" r="12" fill="#1ea3e0"/><path d="M7 12h9M13 8l4 4-4 4" stroke="#fff" stroke-width="2" fill="none"/></svg>
      <p class="bpo__text">We help you design and conduct the right training to fit your organizational needs on-site and virtually. We coach leaders on subjects related to employee engagement to help your organization reach its objectives.</p>
    </div>
    <div class="bpo" style="top:292px">
      <span class="bpo__tag bpo__tag--navy">Back and Front Office</span>
      <svg class="bpo__dot" viewBox="0 0 24 24"><circle cx="12" cy="12" r="12" fill="#0e3b6a"/><path d="M7 12h9M13 8l4 4-4 4" stroke="#fff" stroke-width="2" fill="none"/></svg>
      <p class="bpo__text">With our expertise in engaging employees and unlocking their full potential, we can help you to improve productivity, customer satisfaction, and profitability by outsourcing your back- and front-office functions to us.</p>
    </div>
    <div class="bpo" style="top:400px">
      <span class="bpo__tag bpo__tag--sky">Customer Experience Auditing</span>
      <svg class="bpo__dot" viewBox="0 0 24 24"><circle cx="12" cy="12" r="12" fill="#1ea3e0"/><path d="M7 12h9M13 8l4 4-4 4" stroke="#fff" stroke-width="2" fill="none"/></svg>
      <p class="bpo__text">We can help you monitor and improve your brand's customer experience and sales by assessing the entire customer experience at every stage where the customer interacts with your business, whether face to face, by telephone, or over the web.</p>
    </div>
  </div>
</section>

</body>
</html>
```